Packaging Design For Slatebook Accessories

Pine Harbor Goods (pineharborgoods.example) sells computer accessories to USA retailers. We are developing a line of Slatebook accessories and would like to dramatically improve our current design. The design should feel more upmarket. Use of soft colors, simple graphics and clean fonts (similar to Corvane, Malvex and Tolliver) is something to consider in your design.

Since many of our items are in standard size box we don't require designers to create special box (package) die-line; please use the die-line from the attached Car Charger + Cable artwork and design a theme within our die-line. You can create new icons and graphics, you only need to keep the image of the cable and charger in place (according to die-line)

Artwork of the Screen Protector and Retractable Sync Cable are attached as a **reference only** to the types of items we will be selling. The design theme will be used for most of our products.

The design should resonate with the Quince consumer.
Updates

The budget for this project has been increased.

Designers only need to create art for the Car Charger + Cable.   The die-line is provided, so you only need to design within our die-line.

(all other die-lies are attached for your **reference** as to other items we sell)

Best,
Ned

Reason: The deadline has been extended to provide designers additional time to submit revisions. For those who have not yet submitted initial designs please do so soon. Thank you. Ned

Reason: The deadline has been extended to allow designers appropriate time to make revisions. Because the deadline occurs at 3:49am Australian EST I also want to give extra time over the weekend for those in US/Canada/Europe. Thank you for all for your submissions. Best, Ned

Please submit revisions or initial designs soon.    The deadline will not be extended further as we need to make decision soon.

Thanks to all designers who participated.

Best,
Ned

Target Market(s)

Product will be sold at retail stores in USA.

Target consumer is users of Quince Slatebook, Tunelet, Callbook and other tablet/mobile devices.

Industry/Entity Type

Computer

Requirements
Must have
• Use dieline of the Car Charger + Cable provided. Create new design within the dieline we provided.

Add new icons, new graphics, color as you desire.

Include the copy from the attached artwork.

Use "Built for Slatebook,Callbook,Tunelet" logo provided (attached)
Should not have
• Please do not use simple "all white" design.

```html
<!DOCTYPE html>
<html lang="en">
<head>
<meta charset="utf-8">
<title>USB Car Charger – Packaging Die-line</title>
<link rel="stylesheet" href="https://fonts.googleapis.com/css2?family=Quicksand:wght@400;500;600&family=Arimo&display=swap">
<style>
  :root {
    --rust: #b83200;
    --ink: #1a1a1a;
    --body-ink: #2b2b2b;
    --die-red: #e0302c;
    --panel-grey: #e6e6e6;
    --flap-grey: #ebebeb;
    --dim-blue: #d3e2f5;
    --dim-line: #222;
    --white: #ffffff;
  }
  html, body {
    margin: 0;
    padding: 0;
    width: 1171px;
    height: 1200px;
    overflow: hidden;
    background: var(--white);
  }
  .dieline { display: block; width: 1171px; height: 1200px; }
  .cut { fill: none; stroke: var(--die-red); stroke-width: 1; }
  .dim { stroke: var(--dim-line); stroke-width: 0.8; fill: none; }
  .dim-label { font-family: "Arimo", Arial, sans-serif; font-size: 13px; fill: var(--ink); }
  .title { font-family: "Quicksand", sans-serif; font-weight: 500; }
  .title-dark { fill: var(--ink); }
  .title-rust { fill: var(--rust); }
  .subtitle { font-family: "Quicksand", sans-serif; font-weight: 500; font-size: 17px; fill: var(--ink); }
  .side-title { font-family: "Quicksand", sans-serif; font-weight: 500; fill: var(--white); }
  .copy-heading { font-family: "Quicksand", sans-serif; font-weight: 600; font-size: 12px; fill: var(--rust); }
  .copy-body { font-family: "Quicksand", sans-serif; font-weight: 500; font-size: 7.4px; fill: var(--body-ink); }
  .device-heading { font-family: "Quicksand", sans-serif; font-weight: 500; font-size: 12px; fill: var(--white); }
  .device-name { font-family: "Quicksand", sans-serif; font-weight: 500; font-size: 9px; fill: var(--white); }
  .device-icon { fill: none; stroke: #f2b8a4; stroke-width: 1; }
  .brand-name { font-family: "Quicksand", sans-serif; font-weight: 600; font-size: 9px; fill: #1f4f86; }
</style>
</head>
<body>
<svg class="dieline" viewBox="0 0 880 902" preserveAspectRatio="none" xmlns="http://www.w3.org/2000/svg">
  <defs>
    <linearGradient id="car-tones" x1="0" y1="0" x2="1" y2="1">
      <stop offset="0" stop-color="#4a4d52"/>
      <stop offset="0.5" stop-color="#1c1d20"/>
      <stop offset="1" stop-color="#0b0b0c"/>
    </linearGradient>
    <linearGradient id="cable-tones" x1="0" y1="0" x2="0" y2="1">
      <stop offset="0" stop-color="#f4f4f4"/>
      <stop offset="1" stop-color="#d9d9d9"/>
    </linearGradient>
    <marker id="arrow" viewBox="0 0 10 10" refX="10" refY="5" markerWidth="9" markerHeight="9" orient="auto-start-reverse">
      <path d="M0,1 L10,5 L0,9" fill="none" stroke="#222" stroke-width="1"/>
    </marker>
  </defs>

  <!-- Dimension highlight on right bottom -->
  <rect x="678" y="705" width="119" height="135" fill="var(--dim-blue)"/>

  <!-- Top lid flap -->
  <rect x="319" y="75" width="359" height="125" fill="var(--flap-grey)"/>
  <path class="cut" d="M319,200 V66 Q319,55 330,55 H667 Q678,55 678,66 V200"/>
  <line class="cut" x1="319" y1="75" x2="678" y2="75"/>

  <!-- Left side dust flap -->
  <path class="cut" d="M208,200 V140 H300 L319,160"/>
  <!-- Right side dust flap -->
  <path class="cut" d="M678,160 L690,140 H792 V200"/>

  <!-- Glue flap -->
  <path class="cut" d="M200,200 H190 L172,222 V630 L190,655 H200"/>

  <!-- Side panel -->
  <rect x="200" y="200" width="119" height="455" fill="var(--rust)"/>
  <text class="side-title" font-size="35" transform="translate(258,590) rotate(-90)">USB Car Charger</text>
  <text class="side-title" font-size="17" transform="translate(290,590) rotate(-90)">+charging and sync cable</text>

  <!-- Front panel -->
  <path d="M319,200 H678 V720 H372 Q319,715 319,655 Z" fill="var(--white)"/>
  <text class="title" x="337" y="276" font-size="35"><tspan class="title-dark">USB </tspan><tspan class="title-rust">Car Charger</tspan></text>
  <text class="subtitle" x="650" y="300" text-anchor="end">+charging and sync cable</text>

  <rect x="319" y="335" width="218" height="100" fill="url(#car-tones)" role="img" aria-label="Photo of the car charger plugged into a car's power socket"/>
  <rect x="537" y="335" width="141" height="100" fill="url(#cable-tones)" role="img" aria-label="Photo of the charging and sync cable connectors"/>

  <rect x="319" y="435" width="218" height="220" fill="var(--panel-grey)"/>
  <text class="copy-heading" x="336" y="467">Smart but Powerful</text>
  <text class="copy-body" x="336" y="479">Charge your Slatebook, Callbook or Tunelet at the fastest</text>
  <text class="copy-body" x="336" y="490">possible speed. Get unlimited play and standby</text>
  <text class="copy-body" x="336" y="501">time with the low-profile car charger.</text>
  <text class="copy-heading" x="336" y="540">Features:</text>
  <text class="copy-body" x="336" y="553">Charge your Slatebook, Callbook or Tunelet at the fastest</text>
  <text class="copy-body" x="336" y="564">possible speed. Get unlimited play and standby</text>
  <text class="copy-body" x="336" y="575">time with the low-profile car charger.</text>

  <rect x="537" y="435" width="141" height="220" fill="var(--rust)"/>
  <text class="device-heading" x="579" y="466">Built for</text>
  <rect class="device-icon" x="581" y="483" width="9" height="13" rx="1"/>
  <circle class="device-icon" cx="585.5" cy="492" r="2"/>
  <text class="device-name" x="598" y="494">Tunelet</text>
  <rect class="device-icon" x="581" y="513" width="8" height="15" rx="1.5"/>
  <text class="device-name" x="598" y="524">Callbook</text>
  <rect class="device-icon" x="580" y="545" width="12" height="15" rx="1.5"/>
  <text class="device-name" x="598" y="555">Slatebook</text>

  <text class="brand-name" x="505" y="692" text-anchor="middle">Pine Harbor Goods</text>

  <path class="cut" d="M319,200 V655 Q319,715 372,720 H678"/>

  <!-- Right side panel -->
  <line class="cut" x1="678" y1="200" x2="678" y2="840"/>
  <line class="cut" x1="797" y1="200" x2="797" y2="720"/>
  <line class="cut" x1="678" y1="200" x2="797" y2="200"/>
  <path class="cut" d="M797,720 H792 V780 H690 V720"/>

  <!-- Bottom flap under side panel -->
  <path class="cut" d="M200,655 V835 H319 V655"/>

  <!-- Dimensions -->
  <line class="dim" x1="40" y1="122" x2="215" y2="122"/>
  <line class="dim" x1="40" y1="200" x2="100" y2="200"/>
  <line class="dim" x1="40" y1="720" x2="100" y2="720"/>
  <line class="dim" x1="62" y1="122" x2="62" y2="200" marker-start="url(#arrow)" marker-end="url(#arrow)"/>
  <line class="dim" x1="62" y1="200" x2="62" y2="720" marker-start="url(#arrow)" marker-end="url(#arrow)"/>
  <text class="dim-label" x="28" y="164">1"</text>
  <text class="dim-label" x="26" y="426">6.5"</text>

  <line class="dim" x1="319" y1="720" x2="319" y2="820"/>
  <line class="dim" x1="678" y1="840" x2="678" y2="858"/>
  <line class="dim" x1="797" y1="840" x2="797" y2="858"/>
  <line class="dim" x1="319" y1="796" x2="678" y2="796" marker-start="url(#arrow)" marker-end="url(#arrow)"/>
  <text class="dim-label" x="498" y="792" text-anchor="middle">4.5"</text>
  <line class="dim" x1="678" y1="838" x2="797" y2="838" marker-start="url(#arrow)" marker-end="url(#arrow)"/>
  <text class="dim-label" x="738" y="857" text-anchor="middle">1.5"</text>
</svg>
</body>
</html>
```